New Plumbing Company

We are looking for a smart and creative business card design for our new plumbing company. We are looking for creativity and originality in our business cards.

Industry/Entity Type

Plumbing

Contact Information for Business Card

Crestline Plumbing
Peter Halvane
Managing Director
Telephone Number : 0481529604
Email : service@crestlineplumbing.com.au
Website : www.crestlineplumbing.com.au
Lic. 508264K

Colors
0692cd
33a6d7
000000

Requirements
Must have
• I want the business card to be designed on a black background using the blue tones i have selected as seen in the company logo.

```html
<!DOCTYPE html>
<html lang="en">
<head>
<meta charset="UTF-8">
<title>Crestline Plumbing — Business Card</title>
<link rel="stylesheet" href="https://fonts.googleapis.com/css2?family=Jost:wght@400;500;600&display=swap">
<style>
  :root {
    --stage: #eceeef;
    --card-black: #1f1e1f;
    --card-paper: #e4e6e6;
    --ink: #2b2b2d;
    --brand-blue: #0692cd;
    --brand-blue-light: #33a6d7;
    --brand-white: #f2f3f3;
  }
  * { margin: 0; padding: 0; box-sizing: border-box; }
  html, body {
    width: 1200px;
    height: 800px;
    overflow: hidden;
    background: var(--stage);
    font-family: "Jost", sans-serif;
  }
  .stage {
    width: 1200px;
    height: 800px;
    display: flex;
    align-items: center;
    justify-content: center;
  }
  .business-card {
    width: 900px;
    height: 520px;
    display: flex;
    box-shadow: 0 18px 40px rgba(0, 0, 0, 0.18);
  }
  .brand-panel {
    width: 40%;
    background: var(--card-black);
    display: flex;
    align-items: center;
    justify-content: center;
    gap: 16px;
    padding: 0 24px;
  }
  .brand-dot {
    width: 34px;
    height: 34px;
    border-radius: 50%;
    border: 4px solid var(--brand-blue);
    flex-shrink: 0;
  }
  .brand-name {
    color: var(--brand-white);
    font-weight: 500;
    font-size: 30px;
    letter-spacing: 0.5px;
    line-height: 1.1;
  }
  .contact-panel {
    width: 60%;
    background: var(--card-paper);
    color: var(--ink);
    padding: 110px 0 0 120px;
  }
  .identity {
    text-align: center;
    width: 300px;
    margin-bottom: 54px;
  }
  .person-name {
    font-weight: 600;
    font-size: 26px;
    letter-spacing: 1px;
    text-transform: uppercase;
    line-height: 1.2;
  }
  .person-role,
  .licence {
    font-size: 18px;
    line-height: 1.3;
  }
  .contact-list {
    list-style: none;
    font-size: 18px;
    line-height: 1.9;
  }
</style>
</head>
<body>
  <main class="stage">
    <article class="business-card">
      <section class="brand-panel">
        <span class="brand-dot" aria-hidden="true"></span>
        <span class="brand-name">Crestline Plumbing</span>
      </section>
      <section class="contact-panel">
        <div class="identity">
          <h1 class="person-name">Peter Halvane</h1>
          <p class="person-role">Managing Director</p>
          <p class="licence">Lic. 508264K</p>
        </div>
        <ul class="contact-list">
          <li>Telephone Number : 0481529604</li>
          <li>Email : service@crestlineplumbing.com.au</li>
          <li>Website : www.crestlineplumbing.com.au</li>
        </ul>
      </section>
    </article>
  </main>
</body>
</html>
```